Design four banner ads for our upcoming revamped website

We need four banner ads for our website.

The link of our website is http://beta.mervatrade.com/

The banners will appear under the "Promotions" tab which is currently exhibiting placeholder images.

The titles for each of the banner ads are as follow:
1) Double Credit Chance
2) Capital Protection Scheme
3) Trade Bonus
4) 2.5% Annual Interest

Target Market(s)

forex traders

Requirements
Must have
• The banners must adhere and blend with the website existing theme
Should not have
• Please do not use any human figures in the banner or pictures of humans waving around cash.

```html
<!DOCTYPE html>
<html lang="en">
<head>
<meta charset="utf-8">
<title>Capital Protection Scheme</title>
<link rel="stylesheet" href="https://fonts.googleapis.com/css2?family=Josefin+Sans:wght@700&display=swap">
<style>
  :root {
    --navy: #1f2d3c;
    --navy-deep: #18242f;
    --orange: #f68524;
    --orange-soft: #f9a45a;
    --white: #ffffff;
    --arrow-disc: #7d848b;
    --arrow-mark: #27323e;
  }
  html, body {
    margin: 0;
    padding: 0;
    width: 1200px;
    height: 522px;
    overflow: hidden;
    background: var(--navy);
  }
  .promo-banner {
    position: relative;
    width: 1200px;
    height: 522px;
    overflow: hidden;
    background: var(--navy);
    font-family: "Josefin Sans", "Century Gothic", sans-serif;
  }
  .promo-title {
    position: absolute;
    left: 141px;
    top: 166px;
    margin: 0;
    font-weight: 700;
    font-size: 59px;
    line-height: 69px;
    letter-spacing: 0.5px;
    text-transform: uppercase;
  }
  .promo-title span { display: block; }
  .promo-title .accent { color: var(--orange); }
  .promo-title .plain { color: var(--white); }
  .promo-illustration {
    position: absolute;
    left: 548px;
    top: 60px;
    width: 528px;
    height: 462px;
    border-radius: 48% 48% 12% 12% / 30% 30% 8% 8%;
    background: radial-gradient(ellipse at 50% 38%, var(--orange) 0%, var(--orange-soft) 45%, rgba(255,255,255,0.85) 72%, rgba(255,255,255,0.0) 100%);
  }
  .carousel-arrow {
    position: absolute;
    top: 264px;
    width: 26px;
    height: 26px;
  }
  .carousel-arrow.prev { left: 33px; }
  .carousel-arrow.next { left: 1135px; }
</style>
</head>
<body>
  <main class="promo-banner">
    <h1 class="promo-title">
      <span class="accent">Capital</span>
      <span class="plain">Protection</span>
      <span class="accent">Scheme</span>
    </h1>

    <div class="promo-illustration" role="img" aria-label="Two open hands cradling an orange shield with a black money bag marked with a dollar sign"></div>

    <svg class="carousel-arrow prev" viewBox="0 0 26 26" aria-label="Previous slide" role="img">
      <circle cx="13" cy="13" r="12" fill="var(--arrow-disc)"/>
      <path d="M15.5 7.5 L10 13 L15.5 18.5" fill="none" stroke="var(--arrow-mark)" stroke-width="3.2" stroke-linecap="round" stroke-linejoin="round"/>
    </svg>
    <svg class="carousel-arrow next" viewBox="0 0 26 26" aria-label="Next slide" role="img">
      <circle cx="13" cy="13" r="12" fill="var(--arrow-disc)"/>
      <path d="M10.5 7.5 L16 13 L10.5 18.5" fill="none" stroke="var(--arrow-mark)" stroke-width="3.2" stroke-linecap="round" stroke-linejoin="round"/>
    </svg>
  </main>
</body>
</html>
```